Flyer advertising $25,000 grants available to Pilbara businesses

We need a flyer that will be distributed to local businesses. The idea of the flyer is to let businesses know about some grants that are available for their business, and to let them know we (Corvane Accounting & Finance) can help them successfully apply for the grants.
I have attached some artwork which is currently used as our local phone book advertisement. It would be good if this artwork, or something very similar could feature at the bottom of the flyer, so that businesses know who can help them.

The grants that are being given are for up to $25,000, and are available to businesses based in the Pilbara. The grants won't be available for much longer, so there is a genuine need for businesses to apply very soon or else they will miss out.
To get a $25,000 grant, businesses need to prepare a formal written application. Some applications will be successful, some will not. We have a thorough understanding of the selection criteria for these grants, and we can prepare these applications for local businesses, and give them the best chance of winning one of the $25,000 grants

The Pilbara is a region in the North West of Australia. Its a mining based area that predominately produces iron ore. Most businesses are based around mining services

The flyer will need to be DL sized, ie, 99mm wide and 210mm high. We are only going to print on one side of the flyer.

Target Market(s)

Businesses located in the Pilbara region of Australia that want a $25,000 boost. This regions main industry is iron ore mining, so most businesses are related to the mining industry

Industry/Entity Type

Advertising

Font styles to use
Serif

Requirements
Must have
• Our business details showing somewhere on the flyer. I have attached the ad we put in the local directory as this shows our contact details, and the colour scheme we have used in previous advertising
• Must look professional
Nice to have
• I'm open to different ideas
Should not have

```html
<!DOCTYPE html>
<html lang="en">
<head>
<meta charset="utf-8">
<title>Corvane Accounting &amp; Finance – Grant Flyer</title>
<link rel="stylesheet" href="https://fonts.googleapis.com/css2?family=Barlow:wght@400;600;700&family=Dancing+Script:wght@600&display=swap">
<style>
  :root{
    --stage:#ecebe8;
    --cream:#fbf3ea;
    --blush:#f6dcd8;
    --red:#b0142c;
    --red-dark:#7a0d1e;
    --ink:#2a2a2a;
    --white:#ffffff;
    --strip:#2b1a1c;
    --gold:#e8a46a;
  }
  *{margin:0;padding:0;box-sizing:border-box}
  html,body{width:1200px;height:1000px;overflow:hidden;background:var(--stage)}
  .flyer{
    position:absolute;left:380px;top:35px;width:440px;height:930px;overflow:hidden;
    background:linear-gradient(180deg,var(--cream) 0%,var(--white) 30%,var(--blush) 62%,var(--cream) 72%);
    box-shadow:0 6px 22px rgba(0,0,0,.25);
    font-family:"Barlow",sans-serif;color:var(--ink);
  }
  .flyer-shapes{position:absolute;left:0;top:0}
  .grant-badge{
    position:absolute;right:22px;top:34px;width:128px;height:66px;
    text-align:center;color:var(--white);
  }
  .grant-badge__top,.grant-badge__bottom{font-family:"Dancing Script",cursive;font-size:15px;line-height:1}
  .grant-badge__top{margin-top:6px}
  .grant-badge__amount{font-weight:700;font-size:24px;line-height:1.05}
  .pitch{
    position:absolute;left:24px;top:458px;width:392px;text-align:center;
    font-size:15.5px;line-height:1.3;
  }
  .pitch p+p{margin-top:10px}
  .pitch strong{color:var(--red);font-weight:700}
  .brand-box{
    position:absolute;left:38px;top:698px;width:258px;height:76px;background:var(--white);
    border-radius:12px;box-shadow:0 2px 6px rgba(0,0,0,.3);
    display:flex;align-items:center;justify-content:center;
  }
  .brand-name{font-weight:700;color:var(--red);font-size:20px;text-align:center;line-height:1.1}
  .contact{position:absolute;left:0;top:788px;width:440px;height:90px;color:var(--white)}
  .contact__email{position:absolute;left:34px;top:8px;font-size:17px}
  .contact__licence{position:absolute;left:34px;top:32px;font-size:15px}
  .contact__divider{position:absolute;left:262px;top:10px;width:2px;height:52px;background:var(--white)}
  .contact__phone{position:absolute;left:274px;top:0;font-size:32px;font-weight:700;letter-spacing:1px}
  .contact__web{position:absolute;left:274px;top:40px;font-size:19px;font-weight:700}
  .address-strip{
    position:absolute;left:0;bottom:0;width:440px;height:34px;background:var(--strip);
    color:var(--white);font-size:11px;display:flex;align-items:center;justify-content:center;
  }
</style>
</head>
<body>
<main class="flyer">
  <svg class="flyer-shapes" width="440" height="930" viewBox="0 0 440 930">
    <defs>
      <linearGradient id="photoTone" x1="0" y1="0" x2="0" y2="1">
        <stop offset="0" stop-color="#f4f7ee"/>
        <stop offset=".3" stop-color="#dfe9c6"/>
        <stop offset=".55" stop-color="#f1d6c4"/>
        <stop offset=".75" stop-color="#e6c892"/>
        <stop offset="1" stop-color="#f7f1ec"/>
      </linearGradient>
      <linearGradient id="bandRed" x1="0" y1="0" x2="0" y2="1">
        <stop offset="0" stop-color="#c41a35"/>
        <stop offset="1" stop-color="#6e0b1b"/>
      </linearGradient>
    </defs>
    <!-- red frame behind the lead photo -->
    <circle cx="238" cy="218" r="210" fill="var(--red)"/>
    <!-- lead photo area -->
    <circle cx="250" cy="202" r="195" fill="url(#photoTone)" role="img" aria-label="Photo of cupped hands holding gold coins with a green seedling growing from them"/>
    <!-- black accent arc -->
    <path d="M18 222 A218 218 0 0 0 450 260" fill="none" stroke="#1c1c1c" stroke-width="4"/>
    <!-- badge -->
    <rect x="290" y="34" width="128" height="66" rx="10" fill="var(--red)"/>
    <rect x="294" y="38" width="120" height="58" rx="8" fill="none" stroke="#fff" stroke-opacity=".5"/>
    <!-- bottom band -->
    <path d="M0 690 Q220 650 440 690 L440 930 L0 930 Z" fill="url(#bandRed)"/>
    <path d="M0 684 Q220 644 440 684" fill="none" stroke="var(--gold)" stroke-width="3"/>
  </svg>

  <div class="grant-badge">
    <div class="grant-badge__top">Available up to</div>
    <div class="grant-badge__amount">$25,000</div>
    <div class="grant-badge__bottom">per businesses</div>
  </div>

  <section class="pitch">
    <p>To receive the grant you need to submit an application for why your business should receive the grant over other businesses. Professionally written applications are more likely to win the grants funds.</p>
    <p>We have a thorough understanding of the selection criteria, and what it takes for the grant application to be successful. So far <strong>100% of the applications we have submitted have been successful</strong>, and our clients have enjoyed the benefits of receiving the grant funding.</p>
  </section>

  <div class="brand-box"><span class="brand-name">Corvane<br>Accounting &amp; Finance</span></div>

  <section class="contact">
    <div class="contact__email">reception@cvaf.com.au</div>
    <div class="contact__licence">Australian Credit License 512 846</div>
    <div class="contact__divider"></div>
    <div class="contact__phone">9100 4821</div>
    <div class="contact__web">www.cvaf.com.au</div>
  </section>

  <footer class="address-strip">Shop 3, Harbour Arcade, 12 Kestrel St, Corvane Bay • PO Box 118 Corvane Bay, WA 6722</footer>
</main>
</body>
</html>
```